Corporate Brochure for boutique Australian financial planning firm

We are looking for a face-lift with our company corporate brochure. This brochure will be used to show who we are, what we do, etc. to new potential clients. It will form part of an introductory pack that we give to clients after an initial free consultation.

The target market is generally people over 45 years old, including couples and singles, seeking financial advice.

We have a new logo and would like to implement elements of the logo design into the brochure.

There is a bit of text on the brochure so perhaps 3 double sided A4 pages (6 pages in total) with a trifold might work best.

The colours in our logo are black and red. We are looking to use these colours and maybe also white and grey?

We are after a contemporary, clean, minimalist design using elements/shapes/forms of our logo design in there so it's not generic and speaks out as 'ours'. It needs to be professional but not traditional looking if that makes sense.

This brochure will be used in emails but mostly in print form so it needs to be designed print-ready but in a readable format that we can also send via email.

Here are some things that might help, including attachments:
Our company website: http://corvenwealth.com.au

NOTE
In the New Corporate Brochure Content attachment, the pages have been laid out with printing in mind. So pages 1-3 in the PDF are for the "inside" of the brochure, pages 4-6 are for the "outside" of the brochure. So the front page would be page 6 from the PDF, and the back page would be page 4.

Target Market(s)

Australian couples and singles generally over 45 years old who are seeking financial advice

Industry/Entity Type

Financial Planning

Font styles to use
Sans Serif

Requirements
Must have
• Print-ready for 3 double sided A4 pages (6 pages in total with a trifold)
• Our company logo + other graphics (all in 'Must Use' graphics folder)
• The red colour that's in our logo.
• White background - clean aesthetic.
• Our financial planning process graphic can be kept as is or re-designed to suit space.
Should not have
• Title 'Corporate Brochure'

```html
<!DOCTYPE html>
<html lang="en">
<head>
<meta charset="utf-8">
<title>Corven Wealth – Trifold Brochure Outside</title>
<link rel="stylesheet" href="https://fonts.googleapis.com/css2?family=Source+Sans+3:wght@300;400;600;700&display=swap">
<style>
:root{
  --stage:#c4976a;
  --red:#ee4f3e;
  --red-deep:#e0412f;
  --black:#050505;
  --grey:#9a9a9a;
  --cream:#efebe3;
  --cream-dark:#ddd6c8;
  --ink:#2a2a2a;
  --white:#fff;
}
*{box-sizing:border-box;margin:0;padding:0}
html,body{width:1200px;height:648px;overflow:hidden}
body{background:var(--stage);font-family:"Source Sans 3",Arial,sans-serif;position:relative;color:var(--ink)}
.abs{position:absolute}
.panel-label{position:absolute;top:43px;color:var(--white);font-weight:700;font-size:16px;text-align:center;width:200px}

/* Outside flap */
.flap{left:42px;top:68px;width:372px;height:532px;background:linear-gradient(160deg,#2b2b2b,#0d0d0d 60%,#1a1a1a);box-shadow:2px 3px 6px rgba(0,0,0,.35)}
.team-title{position:absolute;left:0;top:28px;width:302px;height:48px;background:var(--grey);border-radius:0 24px 24px 0;color:var(--white);font-weight:300;font-size:21px;line-height:48px;padding-left:30px}
.team-card{position:absolute;left:76px;top:92px;width:253px;height:390px;background:var(--red)}
.member-photo{position:absolute;left:51px;width:86px;height:106px;background:linear-gradient(160deg,#cfcfcf,#7d7d7d);box-shadow:2px 2px 5px rgba(0,0,0,.4)}
.member{position:absolute;left:152px;width:164px;color:var(--white)}
.member h3{font-size:11px;font-weight:600;margin-bottom:5px}
.member h3 span{font-weight:400;font-size:9px}
.member p{font-size:5.6px;line-height:1.4;margin-bottom:4px;text-align:justify}
.member-rule{position:absolute;left:152px;width:166px;border-top:1px solid rgba(255,255,255,.6)}

/* Back */
.back{left:414px;top:68px;width:368px;height:532px;background:linear-gradient(180deg,var(--red),var(--red-deep));box-shadow:2px 3px 6px rgba(0,0,0,.3)}
.mini-photo{position:absolute;background:linear-gradient(160deg,#d8d8d8,#828282);border:2px solid var(--white);box-shadow:1px 2px 4px rgba(0,0,0,.35)}
.promise-card{position:absolute;left:470px;top:220px;width:249px;height:332px;background:radial-gradient(circle at 50% 40%,#f9f7f2,var(--cream) 60%,var(--cream-dark));box-shadow:2px 3px 6px rgba(0,0,0,.3)}
.promise{position:absolute;left:0;top:10px;width:100%;text-align:center;font-weight:300;font-size:18px;line-height:24.5px;color:#333}
.promise-rule{position:absolute;left:22px;width:206px;top:90px;border-top:1px solid #cfc8bb}
.promise-sub{position:absolute;left:0;top:103px;width:100%;text-align:center;font-weight:300;font-size:14px;line-height:18px;color:#444}
.award-badge{position:absolute;top:276px;width:46px;height:46px;border-radius:50%}
.award-text{position:absolute;left:164px;top:279px;font-size:6.2px;line-height:1.55;color:#333;font-weight:600}

.brand-band{position:absolute;left:454px;top:380px;width:348px;height:98px;background:var(--black);border:5px solid #6d6d6d;border-right:none;box-shadow:0 6px 0 #2a2a2a}
.band-brand{position:absolute;left:87px;top:30px;display:flex;align-items:center;gap:10px}
.band-dash{width:37px;height:5px;background:var(--red)}
.band-name{color:#1d1d1d;font-size:17px;letter-spacing:2px;line-height:1}
.band-tagline{position:absolute;left:82px;top:65px;font-size:5.6px;font-weight:600;color:#5a5a5a;letter-spacing:.3px;white-space:nowrap}

/* Front */
.front{left:782px;top:68px;width:376px;height:532px;background:radial-gradient(circle at 40% 40%,#f3f0ea,#e6e0d4 80%);box-shadow:3px 3px 6px rgba(0,0,0,.35)}
.hero-photo{position:absolute;left:952px;top:84px;width:206px;height:292px;background:linear-gradient(180deg,#dcd8d0,#f1efea 70%)}
.brand-mark{position:absolute;left:840px;top:128px;width:10px;height:10px;background:var(--red)}
.brand-name{position:absolute;left:860px;top:119px;font-size:19px;font-weight:400;letter-spacing:1px;color:#222;line-height:1}
.brand-tag{position:absolute;left:804px;top:160px;font-size:6.4px;color:var(--grey);letter-spacing:.2px;white-space:nowrap}
.bio{position:absolute;left:802px;top:196px;font-size:5.6px;line-height:1.35;color:#666}
.bio p{margin-bottom:6px}
.about-tab{position:absolute;left:802px;top:364px;width:60px;height:120px}
.about-tab span{position:absolute;left:0;width:100%;text-align:center;color:var(--white)}
.advisor-pill{position:absolute;left:856px;top:380px;width:262px;height:98px;background:var(--black);border:4px solid var(--white);border-left:none;border-radius:0 49px 49px 0}
.advisor-pill h2{position:absolute;left:0;width:234px;text-align:center;color:var(--red);font-weight:300;line-height:1;letter-spacing:1px}
.media{position:absolute;font-size:7px;font-weight:600;color:#333;white-space:nowrap}
</style>
</head>
<body>
<div class="panel-label" style="left:114px">Outside flap</div>
<div class="panel-label" style="left:494px">BACK</div>
<div class="panel-label" style="left:868px">FRONT</div>

<!-- Outside flap -->
<section class="abs flap">
  <div class="team-title">Your Corven Wealth Team</div>
  <div class="team-card"></div>
  <div class="member-photo" style="top:106px" role="img" aria-label="Portrait photo of the principal adviser"></div>
  <div class="member-photo" style="top:236px" role="img" aria-label="Portrait photo of the client manager"></div>
  <div class="member-photo" style="top:366px" role="img" aria-label="Portrait photo of the office manager"></div>

  <div class="member" style="top:104px">
    <h3>Marcus Hale <span>(Principal Adviser)</span></h3>
    <p>Marcus is a Chartered Wealth Planner, has a Bachelor of Science (Maths) and is a Super Fund Specialist Adviser.</p>
    <p>He is the founder of Corven Wealth, a privately owned financial planning business based on the Northern Beaches and is one of Australia's only Financial Life Planners.</p>
    <p>Having spent more than 30,000 hours in the financial services industry, Marcus's advice combines left-brain logic with right-brain understanding. He applies his expertise to each client, allowing them to spend their time doing the things that are important to them.</p>
  </div>
  <div class="member-rule" style="top:224px"></div>
  <div class="member" style="top:234px">
    <h3>Rachel Dunmore <span>(Client Manager)</span></h3>
    <p>Rachel holds a Bachelor of Social Science and a Diploma of Financial Services.</p>
    <p>When Marcus makes promises to clients, Rachel is the person that makes sure each and every promise is fulfilled.</p>
    <p>Rachel has worked in the financial services industry since the late 1980s in the UK and Australia.</p>
    <p>Her focus is on providing a reliable, efficient and welcome service for all clients so that they feel at ease with building a long-term relationship with Corven Wealth.</p>
  </div>
  <div class="member-rule" style="top:354px"></div>
  <div class="member" style="top:364px">
    <h3>Mei Lin <span>(Office Manager)</span></h3>
    <p>Mei joined the Corven Wealth team in August 2016.</p>
    <p>Having a background in media and administration, Mei brings a fresh set of eyes to the business, having worked previously outside the financial services industry.</p>
    <p>Her focus is on enhancing communications whilst attending to the day-to-day running of the business.</p>
  </div>
</section>

<!-- Back -->
<section class="abs back"></section>
<div class="mini-photo" style="left:513px;top:122px;width:51px;height:64px" role="img" aria-label="Photo of the client manager"></div>
<div class="mini-photo" style="left:630px;top:122px;width:50px;height:64px" role="img" aria-label="Photo of the office manager"></div>
<div class="mini-photo" style="left:564px;top:114px;width:66px;height:80px" role="img" aria-label="Photo of the principal adviser"></div>

<div class="promise-card">
  <div class="promise">Your Money.<br>Your Values.<br>Your Happiness.</div>
  <div class="promise-rule"></div>
  <div class="promise-sub">Award-Winning Financial Planners<br>on Sydney's Northern Beaches</div>
  <div class="award-badge" style="left:26px;background:#3e5c9c" role="img" aria-label="Adviser of the Year award badge"></div>
  <div class="award-badge" style="left:101px;background:#c9c3b6" role="img" aria-label="Top Rated Planners badge"></div>
  <div class="award-text">Director &amp; Principal Financial<br>Adviser Marcus Hale<br>Winner of the 2016 GWA<br>Adviser of the Year<br>2016 Top Rated Planners</div>
</div>

<div class="brand-band">
  <div class="band-brand"><span class="band-dash"></span><span class="band-name">CORVEN WEALTH</span></div>
  <div class="band-tagline">YOUR MONEY • YOUR VALUES • YOUR HAPPINESS</div>
</div>

<!-- Front -->
<section class="abs front"></section>
<div class="hero-photo" role="img" aria-label="Photo of the principal adviser in a white shirt"></div>
<div class="brand-mark"></div>
<div class="brand-name">CORVEN<br>WEALTH</div>
<div class="brand-tag">YOUR MONEY • YOUR VALUES • YOUR HAPPINESS</div>
<div class="bio">
  <p style="width:198px">Marcus Hale is the Director of Corven Wealth. He was awarded the prestigious 'Adviser of the Year' accolade in 2016 by the Guild of Wealth Advisers and was selected to join the Top Rated Planners group as a result of outstanding feedback from his clients.</p>
  <p style="width:190px">Marcus has a Bachelor of Mathematics. He is an accredited Super Fund Specialist Adviser, a Chartered Wealth Planner and one of Australia's only financial life planners.</p>
  <p style="width:166px">A born and bred Northern Beaches boy, he has an active interest in many sports and with two young boys, you won't see him sitting idle. Between refereeing local football matches, teaching his boys to surf or lining up a birdie putt on the golf course, when he isn't working Marcus is 'on the go'.</p>
  <p style="width:146px">You may have seen him occasionally on Vistacast's Horizon News business program Money Matters Live, or quoted in publications including The Ledger Review or The Harbour Herald.</p>
</div>

<div class="advisor-pill">
  <h2 style="top:10px;font-size:34px">Meet Your</h2>
  <h2 style="top:44px;font-size:40px">ADVISOR</h2>
</div>
<svg class="about-tab" viewBox="0 0 60 120" aria-hidden="true">
  <polygon points="0,18 30,0 60,18 60,120 0,120" fill="#ee4f3e"/>
</svg>
<div class="about-tab">
  <span style="top:26px;font-size:14px;font-weight:300">ABOUT</span>
  <span style="top:46px;font-size:6.8px;font-weight:700;color:#3a1a14">Marcus Hale</span>
</div>

<div class="media" style="left:802px;top:503px">LEDGER REVIEW</div>
<div class="media" style="left:884px;top:503px">The Harbour Herald</div>
<div class="media" style="left:964px;top:503px">Net4</div>
<div class="media" style="left:1000px;top:503px">Sharp Investor</div>
<div class="media" style="left:1074px;top:503px">Daily Courier</div>
<div class="media" style="left:802px;top:533px">Planners Guild</div>
<div class="media" style="left:906px;top:524px;width:22px;height:22px;background:#555" role="img" aria-label="Planner Quarterly listing badge"></div>
<div class="media" style="left:964px;top:533px">Net6</div>
<div class="media" style="left:1000px;top:533px">The Southlander</div>
<div class="media" style="left:1076px;top:531px">Wealth Weekly</div>
<div class="media" style="left:802px;top:566px">The Era</div>
<div class="media" style="left:898px;top:566px">GWA</div>
<div class="media" style="left:964px;top:552px;width:24px;height:24px;border-radius:50%;background:#2f56a0" role="img" aria-label="SFSA specialist badge"></div>
<div class="media" style="left:1000px;top:566px">Horizon Money</div>
<div class="media" style="left:1076px;top:566px">Adviser Digest</div>
</body>
</html>
```